Visually Compelling Flyer Design - Orvane Benefits

We are a life insurance company looking to create visually compelling flyers that gain attention of potential buyers and simplify the concept. It should be professional, friendly, approachable in nature. Our logo and several rough drafts are included.
We are looking to refine this look and make it ultra professional, clean and easy to follow. A creative brief with brand guidelines is also included.
FLYER 1 — PAY YOURSELF FIRST
EYEBROW TAG
YOUR COMPANY JUST UPGRADED YOUR BENEFITS
HEADLINE
One small decision. A lifetime of protection.
SUBHEADLINE
Permanent life insurance + long-term care coverage, starting at $1 a day.
EYEBROW TAG
CHOOSE YOUR DAILY INVESTMENT
STAT — TIER 1
$1 / day → $20,000 Life Insurance
STAT — TIER 2 (HERO — make this one biggest/most prominent)
$2 / day → $40,000 Life Insurance
★ Most Popular
STAT — TIER 3
$3 / day → $60,000 Life Insurance
CAPTION
Rate locked at enrollment. Benefit never decreases.
EYEBROW TAG
THREE BENEFITS. ONE POLICY.
SUBHEADLINE
Your money works three ways.
CALLOUT — BENEFIT 1
01 | Cash Value Growth
BODY
Averages 6% annually over the last 50 years — guaranteed never to fall below 3%. Better than any savings account. And if you ever need it, you can borrow against it. It's your money.
CALLOUT — BENEFIT 2
02 | Tax-Free Death Benefit
BODY
From day one, your family is protected. The full benefit is paid tax-free to the person you choose — no waiting period, no exceptions. That's your legacy, preserved.
CALLOUT — BENEFIT 3
03 | Long-Term Care Coverage
BODY
70% of Americans will need long-term care. This plan pays 75% of your benefit — upfront and tax-free — to cover those costs while you're still alive. Your retirement savings stay intact. Your family stays protected.
EYEBROW TAG
ALREADY HAVE LIFE INSURANCE THROUGH WORK?
SUBHEADLINE
That's term. It ends when you need it most.
BODY
Term life insurance is designed for temporary needs — protecting your paycheck, your mortgage, your kids while they're home. When you retire, the house is paid off and your children are grown. Term ends because the need ends.
BODY
But one need never ends: your final expenses and the cost of long-term care. This permanent plan stays with you after retirement — when term coverage is gone and getting new coverage is expensive or impossible.
COMPARISON — LEFT COLUMN HEADER
✕ TERM LIFE
COMPARISON — LEFT COLUMN ITEMS
Gets more expensive with age
Ends at retirement
No cash value
Temporary protection only
COMPARISON — RIGHT COLUMN HEADER
✓ THIS PLAN
COMPARISON — RIGHT COLUMN ITEMS
Rate locked forever at enrollment
Stays with you after retirement
Builds real cash value
Permanent protection for life
EYEBROW TAG
WHAT MAKES THIS DIFFERENT
SUBHEADLINE
Built for you. Stays with you.
CALLOUT
✓ Guaranteed Issued
No medical exams. No questions asked. You qualify.
CALLOUT
✓ Group Rate
Because you work here, you get pricing individuals can't access on their own.
CALLOUT
✓ Rate Locked Forever
Your premium never increases. Your benefit never decreases.
CALLOUT
✓ Portable
Change jobs. Retire. Your policy comes with you at the same rate.
CALLOUT
✓ Family Coverage
Protect your spouse and children under the same plan.
SUBHEADLINE
Protect retirement. Preserve dignity. Plan ahead.
CTA
Be on the lookout for your personalized coverage details.
CAPTION
Brokered by Orvane Benefits · Underwritten by TrelloraLife
FLYER 2 — THE LONG-TERM CARE REALITY
EYEBROW TAG
WHAT MOST PEOPLE DON'T KNOW — BUT SHOULD
HEADLINE
Most Americans are unprepared. You don't have to be.
SUBHEADLINE
The long-term care gap is real — and it affects families like yours.
EYEBROW TAG
THE NUMBERS ARE HARD TO IGNORE
STAT
70%
of Americans age 65 and older will need some form of long-term care during their lifetime.
CAPTION
Source: Pike & Marsden, Review of Elder Welfare and Civic Planning, 2018
STAT
3–4%
of Americans over 50 own a private long-term care insurance policy. The gap between who needs it and who has it is staggering.
CAPTION
Source: Dunn & Solberg, QRT Wellness Wire, 2023
STAT
$700 Billion+
Estimated annual U.S. long-term care cost — and it's growing every year.
CAPTION
Source: Brandt Lowe & Petrasek, Civic Policy Roundtable, 2020
STAT
$470 Billion
The estimated value of unpaid care provided by family members every year. That's the real cost — measured in time, stress, and financial sacrifice.
CAPTION
Source: Lindqvist & Oram, Harborline Institute
STAT
80%
of total long-term care spending goes directly to assist retirees. This isn't a young person's problem. But the time to plan is now.
CAPTION
SUBHEADLINE
Long-term care doesn't just cost money. It costs families.
BODY
When there's no plan in place, the people you love absorb the impact — financially, emotionally, and physically. Retirement savings built over a lifetime can disappear in months. Family members step back from their own lives to provide care. Dignity becomes a daily negotiation.
BODY
This is not inevitable. A small decision today changes the entire outcome.
EYEBROW TAG
THE SOLUTION
HEADLINE
The Pay Yourself First Principle.
BODY
Take the first $1, $2, or $3 you make every day and invest it in a permanent life insurance policy that includes long-term care coverage — underwritten by TrelloraLife, offered through your employer at a group rate, and Guaranteed Issued for everyone.
STAT
$1 / day → $20,000 $2 / day → $40,000 $3 / day → $60,000
BODY
The benefit includes three protections in one: a cash value that grows at an average of 6% annually, a tax-free death benefit for your family, and long-term care coverage that pays 75% of your benefit upfront — tax-free — when you need care most.
SUBHEADLINE
Whether you're single, married, with children or without — there is protection in this plan for you.
HEADLINE
CTA
Look for your personalized offer. Coverage details are coming your way.
CAPTION
COPY RULES FOR DESIGNERS
Headlines are one idea only. Never more than two lines.
Stats stand alone. Never buried in a paragraph.
Body copy maxes at 3 sentences per block. If it's longer, cut it.
The $2/day tier is always the hero. Always.
"Guaranteed Issued" appears on both flyers. It's the most important trust signal.
TrelloraLife is always attributed. Always.
The tagline is: Protect retirement. Preserve dignity. Plan ahead. — Use it verbatim.
Target Market(s)
Average Americans with a family - adults looking for life insurance
Industry/Entity Type
Life Insurance & Financial Retirement

```html
<!DOCTYPE html>
<html lang="en">
<head>
<meta charset="utf-8">
<title>Orvane Benefits — Flyers</title>
<link href="https://fonts.googleapis.com/css2?family=Outfit:wght@400;500;600;700;800&family=Inter:wght@400;500;600&family=Barlow+Condensed:wght@600;700&display=swap" rel="stylesheet">
<style>
:root{
  --stage:#1e2126;
  --navy:#1f2c72;
  --navy-deep:#17225e;
  --blue:#1e5fc0;
  --teal:#1aa3c8;
  --teal-light:#5fc4de;
  --ink:#2b2f3a;
  --muted:#555b68;
  --line:#9fcfe2;
  --mist:#e8f4fb;
  --grey:#efefef;
  --red:#e0424a;
  --green:#22b07a;
}
*{margin:0;padding:0;box-sizing:border-box}
html,body{width:1200px;height:774px;overflow:hidden;background:var(--stage)}
body{position:relative;font-family:"Inter",sans-serif;color:var(--ink)}
.flyer{position:absolute;top:55px;width:518px;height:670px;background:#fff;overflow:hidden}
.flyer--plan{left:55px}
.flyer--reality{left:610px}
.abs{position:absolute}
.heading{font-family:"Outfit",sans-serif}

.photo{position:absolute;top:0;right:0;
  -webkit-mask-image:linear-gradient(to bottom,#000 60%,transparent),linear-gradient(to right,transparent,#000 30%);
  -webkit-mask-composite:source-in;mask-composite:intersect;
  mask-image:linear-gradient(to bottom,#000 60%,transparent),linear-gradient(to right,transparent,#000 30%);}
.photo--plan{width:300px;height:210px;background:linear-gradient(180deg,#6fa9e0 0%,#a9cdea 35%,#d9e4ea 55%,#e9d8c3 80%,#f3ece3 100%)}
.photo--reality{width:210px;height:265px;background:linear-gradient(180deg,#c9d2d8 0%,#b9c6cf 30%,#d8d2c8 60%,#efe7dc 100%)}

.brand{position:absolute;left:28px;top:20px;display:flex;align-items:center;gap:6px}
.brand__dot{width:52px;height:52px;border-radius:50%;background:var(--blue)}
.brand__name{font-family:"Outfit",sans-serif;font-weight:600;font-size:18px;line-height:16px;color:var(--blue);letter-spacing:.3px}

.seal{position:absolute;left:255px;top:22px;width:68px;height:68px;border-radius:50%;
  background:radial-gradient(circle at 40% 35%,var(--blue),var(--navy));box-shadow:0 0 0 3px #fff inset,0 0 0 4px var(--navy) inset;
  display:flex;align-items:center;justify-content:center;text-align:center;transform:rotate(-8deg);
  font-family:"Outfit",sans-serif;font-weight:800;font-size:9px;line-height:10px;color:#fff}

.headline{position:absolute;left:31px;font-family:"Outfit",sans-serif;font-weight:800;color:var(--navy);font-size:26.5px;line-height:28px;letter-spacing:-.3px}
.lede{position:absolute;left:31px;font-size:11.5px;line-height:15px;color:var(--ink)}
.lede b{color:var(--teal);font-weight:600}

.eyebrow{position:absolute;font-family:"Outfit",sans-serif;font-weight:700;color:var(--navy);font-size:10.5px;letter-spacing:.1px;white-space:nowrap}
.rule{position:absolute;height:1px;background:var(--line)}
.sub{position:absolute;font-size:8.5px;color:var(--ink)}

/* tiers, plan */
.tier{position:absolute;top:217px;width:135px;height:100px;border-radius:14px;border:1px solid #d9dde2;background:#fff;text-align:center}
.tier--hero{border:none;background:linear-gradient(135deg,var(--blue),var(--navy-deep));color:#fff}
.tier__tab{position:absolute;left:-8px;top:22px;width:18px;height:46px;border-radius:9px;background:linear-gradient(var(--teal),var(--navy));
  color:#fff;font-family:"Outfit",sans-serif;font-weight:700;font-size:7.5px;display:flex;align-items:center;justify-content:center;writing-mode:vertical-rl;transform:rotate(180deg)}
.tier--hero .tier__tab{background:var(--teal-light)}
.tier__flag{position:absolute;right:0;top:0;width:19px;height:100%;background:var(--navy-deep);border-radius:0 14px 14px 0;
  color:#fff;font-family:"Outfit",sans-serif;font-weight:700;font-size:6.5px;display:flex;align-items:center;justify-content:center;writing-mode:vertical-rl;transform:rotate(180deg);border-radius:14px 0 0 14px}
.tier__price{margin-top:8px;font-family:"Outfit",sans-serif;font-weight:800;font-size:30px;line-height:32px;color:var(--teal)}
.tier--hero .tier__price{color:#fff}
.tier__price small{font-size:9px;font-weight:500;vertical-align:4px;margin-left:3px}
.tier__arrow{display:block;margin:2px auto 0}
.tier__amount{font-family:"Outfit",sans-serif;font-weight:800;font-size:17px;line-height:20px;color:var(--navy);margin-top:3px}
.tier--hero .tier__amount{color:#fff}
.tier__label{font-family:"Outfit",sans-serif;font-weight:600;font-size:8.5px;color:var(--navy)}
.tier--hero .tier__label{color:#fff}
.lock-note{position:absolute;top:326px;left:0;width:518px;text-align:center;font-size:8px;color:var(--ink)}

.benefit{position:absolute;left:31px;width:160px}
.benefit__icon{position:absolute;left:0;top:0}
.benefit__title{margin-left:30px;font-family:"Outfit",sans-serif;font-weight:600;font-size:8.5px;color:var(--teal)}
.benefit__title span{font-weight:400}
.benefit__body{margin-left:30px;margin-top:3px;font-size:5.3px;line-height:7.2px;color:var(--muted)}
.spine{position:absolute;left:43px;top:408px;height:132px;border-left:1px dotted var(--teal)}
.divider{position:absolute;left:195px;top:357px;height:195px;width:1px;background:#e2e5ea}

.copy{position:absolute;font-size:5.4px;line-height:7.3px;color:var(--muted)}
.compare{position:absolute;top:434px;height:63px;width:128px;border-radius:11px;padding:7px 12px}
.compare--term{left:213px;background:var(--grey)}
.compare--plan{left:348px;background:var(--mist)}
.compare__head{font-family:"Outfit",sans-serif;font-weight:500;font-size:8.5px;color:var(--navy);display:flex;align-items:center;gap:3px;margin-bottom:4px}
.compare li{list-style:none;font-size:5.3px;line-height:7.3px;display:flex;align-items:center;gap:3px}
.mark{width:6px;height:6px;border-radius:50%;flex:none}
.mark--x{background:var(--red)}
.mark--ok{background:var(--green)}
.compare__head .mark{width:8px;height:8px}

.feature{position:absolute;top:553px;width:58px}
.feature__title{margin-top:8px;font-family:"Outfit",sans-serif;font-weight:600;font-size:8.5px;line-height:9.5px;color:var(--navy)}
.feature__body{margin-top:4px;font-size:5.3px;line-height:7.2px;color:var(--muted)}

.cta{position:absolute;top:557px;width:165px;height:113px;border-radius:14px 14px 0 0;background:linear-gradient(160deg,var(--blue),var(--navy-deep));color:#fff;padding:10px 10px 0}
.cta__tag{margin-left:42px;font-family:"Outfit",sans-serif;font-weight:600;font-size:10px;line-height:12px}
.cta__tag span{color:var(--teal-light)}
.cta__hr{border-top:1px dashed rgba(255,255,255,.5);margin-top:9px}
.cta__note{display:flex;align-items:center;gap:6px;padding:6px 6px;font-size:5.6px;line-height:7px}
.cta__mail{width:21px;height:21px;border-radius:50%;background:var(--teal-light);flex:none;display:flex;align-items:center;justify-content:center}
.cta__foot{text-align:center;font-size:4.6px;padding-top:6px}
.band{position:absolute;left:0;bottom:0;width:518px;height:8px;background:linear-gradient(90deg,var(--navy),var(--blue),var(--teal))}

/* reality flyer */
.stat{position:absolute}
.stat__num{font-family:"Barlow Condensed",sans-serif;font-weight:700;color:var(--blue);font-size:24px;line-height:24px}
.stat__num--wide{font-size:23px}
.stat__text{font-family:"Outfit",sans-serif;font-size:6.6px;line-height:7.8px;color:var(--navy);margin-top:3px}
.stat__src{font-size:5.1px;line-height:7px;color:var(--muted);font-style:italic;margin-top:5px}
.impact{position:absolute;left:352px;top:241px;width:140px;height:160px;border-radius:10px;background:var(--mist);padding:28px 13px 0}
.impact__icon{position:absolute;left:11px;top:-17px}
.impact__title{font-family:"Outfit",sans-serif;font-weight:700;font-size:10px;line-height:13px;color:var(--navy)}
.impact__body{margin-top:8px;font-size:5.3px;line-height:7.2px;color:var(--muted)}
.solution{position:absolute;left:33px;top:418px;width:460px;height:74px;border-radius:14px;background:linear-gradient(90deg,var(--navy-deep),var(--blue) 70%,#1b78c8)}
.solution__tag{position:absolute;left:18px;top:11px;font-family:"Outfit",sans-serif;font-weight:500;font-size:9.5px;color:var(--teal-light)}
.solution__title{position:absolute;left:20px;top:24px;font-family:"Outfit",sans-serif;font-weight:700;font-size:13px;color:#fff;white-space:nowrap}
.solution__body{position:absolute;left:214px;top:17px;width:230px;font-size:5.3px;line-height:7.2px;color:#e4ecf8}
.pill{position:absolute;top:470px;width:135px;height:69px;border-radius:14px;background:var(--grey);box-shadow:0 1px 3px rgba(0,0,0,.15);padding:10px 0 0 18px}
.pill--hero{background:linear-gradient(135deg,#1a8fd0,var(--teal));color:#fff}
.pill__price{font-family:"Outfit",sans-serif;font-weight:800;font-size:27px;line-height:27px;color:var(--teal)}
.pill--hero .pill__price{color:#fff}
.pill__price small{font-size:8.5px;font-weight:500;vertical-align:3px;margin-left:3px}
.pill__row{display:flex;align-items:center;gap:6px;margin-top:3px;font-family:"Outfit",sans-serif;font-weight:700;font-size:13px;color:var(--navy)}
.pill--hero .pill__row{color:#fff}
.pill__badge{position:absolute;top:-9px;left:58px;background:var(--navy);color:#fff;border-radius:9px 9px 0 0;font-family:"Outfit",sans-serif;font-weight:600;font-size:6.5px;padding:3px 7px}
.closer{position:absolute;left:37px;top:590px;width:280px;font-family:"Outfit",sans-serif;font-weight:700;font-size:10.7px;line-height:14px;color:var(--navy)}
</style>
</head>
<body>

<!-- Flyer 1: Pay Yourself First -->
<section class="flyer flyer--plan">
  <div class="photo photo--plan" role="img" aria-label="Photo of a smiling family of three walking hand in hand along a sunny beach"></div>

  <div class="brand"><div class="brand__dot"></div><div class="brand__name">ORVANE<br>BENEFITS</div></div>
  <div class="seal">GUARANTEED<br>ISSUED</div>

  <h1 class="headline" style="top:90px">One small decision.<br>A lifetime of protection.</h1>
  <p class="lede" style="top:149px">Permanent life insurance + long-term care<br>coverage, starting at <b>$1 a day.</b></p>

  <div class="rule" style="left:33px;top:205px;width:133px"></div>
  <div class="eyebrow" style="left:174px;top:198px">CHOOSE YOUR DAILY INVESTMENT</div>
  <div class="rule" style="left:348px;top:205px;width:147px"></div>

  <div class="tier" style="left:41px">
    <div class="tier__tab">TIER 1</div>
    <div class="tier__price">$1<small>/ day</small></div>
    <svg class="tier__arrow" width="24" height="6" viewBox="0 0 24 6"><path d="M0 3H21" stroke="#1f2c72" stroke-width="1"/><path d="M19 0.5L23 3L19 5.5Z" fill="#1f2c72"/></svg>
    <div class="tier__amount">$20,000</div>
    <div class="tier__label">Life Insurance</div>
  </div>
  <div class="tier tier--hero" style="left:199px">
    <div class="tier__tab">TIER 2</div>
    <div class="tier__flag">★ MOST POPULAR</div>
    <div class="tier__price" style="margin-right:14px">$2<small>/ day</small></div>
    <svg class="tier__arrow" width="24" height="6" viewBox="0 0 24 6" style="margin-left:46px"><path d="M0 3H21" stroke="#fff" stroke-width="1"/><path d="M19 0.5L23 3L19 5.5Z" fill="#fff"/></svg>
    <div class="tier__amount" style="margin-right:14px">$40,000</div>
    <div class="tier__label" style="margin-right:14px">Life Insurance</div>
  </div>
  <div class="tier" style="left:357px">
    <div class="tier__tab">TIER 1</div>
    <div class="tier__price">$3<small>/ day</small></div>
    <svg class="tier__arrow" width="24" height="6" viewBox="0 0 24 6"><path d="M0 3H21" stroke="#1f2c72" stroke-width="1"/><path d="M19 0.5L23 3L19 5.5Z" fill="#1f2c72"/></svg>
    <div class="tier__amount">$60,000</div>
    <div class="tier__label">Life Insurance</div>
  </div>

  <div class="rule" style="left:33px;top:332px;width:115px"></div>
  <p class="lock-note">
    <svg width="6" height="7" viewBox="0 0 6 7" style="vertical-align:-1px"><rect x="0.5" y="3" width="5" height="4" rx="0.6" fill="#2b2f3a"/><path d="M1.5 3V2a1.5 1.5 0 0 1 3 0v1" stroke="#2b2f3a" fill="none"/></svg>
    Rate locked at enrollment. Benefit never decreases.</p>
  <div class="rule" style="left:371px;top:332px;width:124px"></div>

  <div class="eyebrow" style="left:31px;top:357px">THREE BENEFITS. ONE POLICY.</div>
  <p class="sub" style="left:31px;top:372px">Your money works three ways.</p>

  <div class="spine"></div>
  <div class="benefit" style="top:387px">
    <svg class="benefit__icon" width="24" height="27" viewBox="0 0 24 27"><path d="M12 1L23 5V13C23 20 18 24 12 26C6 24 1 20 1 13V5Z" fill="#1e5fc0"/><path d="M6 18V15M9 18V12M12 18V14M15 18V10M18 18V8" stroke="#fff" stroke-width="1.5"/></svg>
    <div class="benefit__title"><span>01 |</span> Cash Value Growth</div>
    <p class="benefit__body">Averages 6% annually over the last 50 years — guaranteed never to fall below 3%. Better than any savings account. And if you ever need it, you can borrow against it. It's your money.</p>
  </div>
  <div class="benefit" style="top:440px">
    <svg class="benefit__icon" width="24" height="27" viewBox="0 0 24 27"><path d="M12 1L23 5V13C23 20 18 24 12 26C6 24 1 20 1 13V5Z" fill="#1e5fc0"/><rect x="7" y="8" width="10" height="8" rx="1" fill="none" stroke="#fff" stroke-width="1.2"/><circle cx="12" cy="12" r="2" fill="#fff"/></svg>
    <div class="benefit__title"><span>02 |</span> Tax-Free Death Benefit</div>
    <p class="benefit__body">From day one, your family is protected. The full benefit is paid tax-free to the person you choose — no waiting period, no exceptions. That's your legacy, preserved.</p>
  </div>
  <div class="benefit" style="top:494px">
    <svg class="benefit__icon" width="24" height="27" viewBox="0 0 24 27"><path d="M12 1L23 5V13C23 20 18 24 12 26C6 24 1 20 1 13V5Z" fill="#1e5fc0"/><path d="M12 15C8 12 8 8 10 8C11 8 12 9 12 10C12 9 13 8 14 8C16 8 16 12 12 15Z" fill="#fff"/><path d="M6 14C7 17 9 18 12 19C15 18 17 17 18 14" stroke="#fff" fill="none" stroke-width="1.2"/></svg>
    <div class="benefit__title"><span>03 |</span> Long-Term Care Coverage</div>
    <p class="benefit__body">70% of Americans will need long-term care. This plan pays 75% of your benefit — upfront and tax-free — to cover those costs while you're still alive. Your retirement savings stay intact. Your family stays protected.</p>
  </div>

  <div class="divider"></div>

  <div class="eyebrow" style="left:213px;top:357px">ALREADY HAVE LIFE INSURANCE THROUGH WORK?</div>
  <p class="sub" style="left:213px;top:372px">That's term. It ends when you need it most.</p>
  <p class="copy" style="left:213px;top:386px;width:127px">Term life insurance is designed for temporary needs — protecting your paycheck, your mortgage, your kids while they're home. When you retire, the house is paid off and your children are grown. Term ends because the need ends.</p>
  <p class="copy" style="left:348px;top:386px;width:140px">But one need never ends: your final expenses and the cost of long-term care. This permanent plan stays with you after retirement — when term coverage is gone and getting new coverage is expensive or impossible.</p>

  <div class="compare compare--term">
    <div class="compare__head"><span class="mark mark--x"></span>TERM LIFE</div>
    <ul>
      <li><span class="mark mark--x"></span>Gets more expensive with age</li>
      <li><span class="mark mark--x"></span>Ends at retirement</li>
      <li><span class="mark mark--x"></span>No cash value</li>
      <li><span class="mark mark--x"></span>Temporary protection only</li>
    </ul>
  </div>
  <div class="compare compare--plan">
    <div class="compare__head"><span class="mark mark--ok"></span>THIS PLAN</div>
    <ul>
      <li><span class="mark mark--ok"></span>Rate locked forever at enrollment</li>
      <li><span class="mark mark--ok"></span>Stays with you after retirement</li>
      <li><span class="mark mark--ok"></span>Builds real cash value</li>
      <li><span class="mark mark--ok"></span>Permanent protection for life</li>
    </ul>
  </div>

  <div class="eyebrow" style="left:213px;top:522px">WHAT MAKES THIS DIFFERENT</div>
  <div class="rule" style="left:364px;top:529px;width:131px"></div>
  <p class="sub" style="left:213px;top:538px">Built for you. Stays with you.</p>

  <div class="feature" style="left:213px">
    <svg width="24" height="24" viewBox="0 0 24 24" fill="none" stroke="#1e5fc0" stroke-width="1.2"><rect x="2" y="2" width="20" height="16" rx="1.5"/><path d="M1 21H23"/><path d="M12 5L17 7V11C17 14 15 15.5 12 16.5C9 15.5 7 14 7 11V7Z"/><path d="M9.5 10.5L11.3 12.3L14.5 9"/></svg>
    <div class="feature__title">Guaranteed Issued</div>
    <p class="feature__body">No medical exams. No questions asked. You qualify.</p>
  </div>
  <div class="feature" style="left:277px">
    <svg width="24" height="24" viewBox="0 0 24 24" fill="none" stroke="#1e5fc0" stroke-width="1.2"><circle cx="12" cy="5" r="2.5"/><circle cx="6" cy="8" r="2.2"/><circle cx="18" cy="8" r="2.2"/><path d="M8 16C8 12 16 12 16 16M2 18C2 14 8 13 9 14M22 18C22 14 16 13 15 14M3 22H21"/></svg>
    <div class="feature__title">Group<br>Rate</div>
    <p class="feature__body">Because you work here, you get pricing individuals can't access on their own.</p>
  </div>
  <div class="feature" style="left:338px">
    <svg width="24" height="24" viewBox="0 0 24 24" fill="none" stroke="#1e5fc0" stroke-width="1.2"><rect x="5" y="10" width="14" height="12" rx="1.5"/><path d="M8 10V6a4 4 0 0 1 8 0v4"/><circle cx="12" cy="15" r="1.5" fill="#1e5fc0"/><path d="M12 16.5V19"/></svg>
    <div class="feature__title">Rate Locked Forever</div>
    <p class="feature__body">Your premium never increases. Your benefit never decreases.</p>
  </div>
  <div class="feature" style="left:401px">
    <svg width="24" height="24" viewBox="0 0 24 24" fill="none" stroke="#1e5fc0" stroke-width="1.2"><rect x="1" y="7" width="17" height="12" rx="1.5"/><path d="M7 7V4H12V7"/><circle cx="17" cy="14" r="4.5" fill="#fff"/><path d="M20.5 17.5L23 20"/></svg>
    <div class="feature__title">Portable</div>
    <p class="feature__body">Change jobs. Retire. Your policy comes with you at the same rate.</p>
  </div>
  <div class="feature" style="left:461px">
    <svg width="24" height="24" viewBox="0 0 24 24" fill="none" stroke="#1e5fc0" stroke-width="1.2"><circle cx="9" cy="5" r="2"/><circle cx="15" cy="5" r="2"/><circle cx="12" cy="10" r="1.6"/><path d="M6 13C6 9 12 9 12 11C12 9 18 9 18 13"/><path d="M2 17L8 16L14 18L21 15M2 21H12L22 18"/></svg>
    <div class="feature__title">Family Coverage</div>
    <p class="feature__body">Protect your spouse and children under the same plan.</p>
  </div>

  <div class="cta" style="left:31px">
    <svg class="abs" style="left:12px;top:10px" width="34" height="34" viewBox="0 0 34 34" fill="none" stroke="#fff" stroke-width="1.3"><path d="M18 2L30 6V14C30 21 25 25 18 27C11 25 6 21 6 14V6Z"/><path d="M11 14A7 7 0 0 1 25 14Z"/><path d="M18 14V20"/><path d="M2 24L9 22L16 25L24 22M2 30H14L26 26"/></svg>
    <div class="cta__tag">Protect retirement.<br><span>Preserve dignity.</span><br>Plan ahead.</div>
    <div class="cta__hr"></div>
    <div class="cta__note">
      <div class="cta__mail"><svg width="11" height="8" viewBox="0 0 11 8" fill="none" stroke="#fff" stroke-width="0.9"><rect x="0.5" y="0.5" width="10" height="7"/><path d="M0.5 0.5L5.5 4.5L10.5 0.5"/></svg></div>
      <span>Be on the lookout for your personalized coverage details.</span>
    </div>
    <div class="cta__hr" style="margin-top:2px"></div>
    <p class="cta__foot">Brokered by Orvane Benefits · Underwritten by <b>TrelloraLife</b></p>
  </div>
  <div class="band"></div>
</section>

<!-- Flyer 2: The Long-Term Care Reality -->
<section class="flyer flyer--reality">
  <div class="photo photo--reality" role="img" aria-label="Photo of a family of four seen from behind, walking along the shoreline"></div>

  <div class="brand"><div class="brand__dot"></div><div class="brand__name">ORVANE<br>BENEFITS</div></div>
  <div class="seal">GUARANTEED<br>ISSUED</div>

  <h1 class="headline" style="top:90px;left:32px">Most Americans<br>are unprepared.<br>You don't have to be.</h1>
  <p class="lede" style="top:174px;left:32px">The long-term care gap is real — and it affects<br>families like yours.</p>

  <div class="eyebrow" style="left:32px;top:219px">THE NUMBERS ARE HARD TO IGNORE</div>
  <div class="rule" style="left:216px;top:226px;width:124px"></div>

  <div class="stat" style="left:33px;top:242px;width:80px">
    <div class="stat__num">70%</div>
    <p class="stat__text">of Americans age 65 and older will need some form of long-term care during their lifetime.</p>
    <p class="stat__src">Source: Pike &amp; Marsden, Review of Elder Welfare and Civic Planning, 2018</p>
  </div>
  <div class="stat" style="left:126px;top:242px;width:84px">
    <div class="stat__num">3–4%</div>
    <p class="stat__text">of Americans over 50 own a private long-term care insurance policy. The gap between who needs it and who has it is staggering.</p>
    <p class="stat__src">Source: Dunn &amp; Solberg,<br>QRT Wellness Wire, 2023</p>
  </div>
  <div class="stat" style="left:222px;top:242px;width:118px">
    <div class="stat__num">80%</div>
    <p class="stat__text">of total long-term care spending goes directly to assist retirees. This isn't a young person's problem. But the time to plan is now.</p>
    <p class="stat__src">Source: Lindqvist &amp; Oram, Harborline Institute</p>
  </div>
  <div class="stat" style="left:33px;top:343px;width:124px">
    <div class="stat__num stat__num--wide">$700 Billion+</div>
    <p class="stat__text">Estimated annual U.S. long-term care cost — and it's growing every year.</p>
    <p class="stat__src">Source: Brandt Lowe &amp; Petrasek,<br>Civic Policy Roundtable, 2020</p>
  </div>
  <div class="stat" style="left:166px;top:343px;width:176px">
    <div class="stat__num stat__num--wide">$470 Billion</div>
    <p class="stat__text">The estimated value of unpaid care provided by family members every year. That's the real cost — measured in time, stress, and financial sacrifice.</p>
    <p class="stat__src">Source: Lindqvist &amp; Oram, Harborline Institute</p>
  </div>

  <div class="impact">
    <svg class="impact__icon" width="32" height="36" viewBox="0 0 32 36"><path d="M16 1L31 6V17C31 26 24 32 16 35C8 32 1 26 1 17V6Z" fill="#1e5fc0"/><path d="M16 19C11 15 11 10 13.5 10C15 10 16 11.5 16 12.5C16 11.5 17 10 18.5 10C21 10 21 15 16 19Z" fill="none" stroke="#fff" stroke-width="1.3"/><path d="M8 18C9 23 12 24 16 25C20 24 23 23 24 18" stroke="#fff" fill="none" stroke-width="1.3"/></svg>
    <div class="impact__title">Long-term care<br>doesn't just cost money.<br>It costs families.</div>
    <p class="impact__body">When there's no plan in place, the people you love absorb the impact — financially, emotionally, and physically. Retirement savings built over a lifetime can disappear in months. Family members step back from their own lives to provide care. Dignity becomes a daily negotiation.</p>
    <p class="impact__body" style="margin-top:8px">This is not inevitable. A small decision today changes the entire outcome.</p>
  </div>

  <div class="solution">
    <div class="solution__tag">THE SOLUTION</div>
    <div class="solution__title">The Pay Yourself First Principle.</div>
    <p class="solution__body">Take the first <b style="color:#fff">$1, $2, or $3</b> you make every day and invest it in a permanent life insurance policy that includes long-term care coverage — underwritten by TrelloraLife, offered through your employer at a group rate, and Guaranteed Issued for everyone.</p>
  </div>

  <div class="pill" style="left:50px">
    <div class="pill__price">$1<small>/ day</small></div>
    <div class="pill__row">$20,000<svg width="48" height="6" viewBox="0 0 48 6"><path d="M0 3H45" stroke="#1f2c72"/><path d="M43 0.5L47.5 3L43 5.5Z" fill="#1f2c72"/></svg></div>
  </div>
  <div class="pill pill--hero" style="left:194px">
    <div class="pill__badge">★ MOST POPULAR</div>
    <div class="pill__price">$2<small>/ day</small></div>
    <div class="pill__row">$40,000<svg width="48" height="6" viewBox="0 0 48 6"><path d="M0 3H45" stroke="#fff"/><path d="M43 0.5L47.5 3L43 5.5Z" fill="#fff"/></svg></div>
  </div>
  <div class="pill" style="left:338px">
    <div class="pill__price">$3<small>/ day</small></div>
    <div class="pill__row">$60,000<svg width="48" height="6" viewBox="0 0 48 6"><path d="M0 3H45" stroke="#1f2c72"/><path d="M43 0.5L47.5 3L43 5.5Z" fill="#1f2c72"/></svg></div>
  </div>

  <p class="copy" style="left:37px;top:556px;width:278px;font-size:6px;line-height:7.8px;color:var(--ink)">The benefit includes three protections in one: a cash value that grows at an average of 6% annually, a tax-free death benefit for your family, and long-term care coverage that pays 75% of your benefit upfront — tax-free — when you need care most.</p>
  <p class="closer">Whether you're single, married, with children or without — there is protection in this plan for you.</p>

  <div class="cta" style="left:331px">
    <svg class="abs" style="left:12px;top:10px" width="34" height="34" viewBox="0 0 34 34" fill="none" stroke="#fff" stroke-width="1.3"><path d="M18 2L30 6V14C30 21 25 25 18 27C11 25 6 21 6 14V6Z"/><path d="M11 14A7 7 0 0 1 25 14Z"/><path d="M18 14V20"/><path d="M2 24L9 22L16 25L24 22M2 30H14L26 26"/></svg>
    <div class="cta__tag">Protect retirement.<br><span>Preserve dignity.</span><br>Plan ahead.</div>
    <div class="cta__hr"></div>
    <div class="cta__note">
      <div class="cta__mail"><svg width="11" height="8" viewBox="0 0 11 8" fill="none" stroke="#fff" stroke-width="0.9"><rect x="0.5" y="0.5" width="10" height="7"/><path d="M0.5 0.5L5.5 4.5L10.5 0.5"/></svg></div>
      <span>Look for your personalized offer. Coverage details are coming your way.</span>
    </div>
    <div class="cta__hr" style="margin-top:2px"></div>
    <p class="cta__foot">Brokered by Orvane Benefits · Underwritten by <b>TrelloraLife</b></p>
  </div>
  <div class="band"></div>
</section>

</body>
</html>
```